Awesome Valdren Business Card Project

We would like a double-sided business card. We have a primary PMS color of PMS 1505 and a secondary color of PMS 1495. I would like to include our logo, the secondary S logo, and the QTALX logo on the business card. We will want a spot for the following information.
Marisa Colton
Valdren
Address: 4318 N Fable Avenue Oak Terrace, IL 60291
Email: mcolton@valdren.example
Phone: 312-555-0148
Mobile: (414) 555-0193
Website: www.valdren.example
Contact Information for Business Card
Marisa Colton Valdren Address: 4318 N Fable Avenue Oak Terrace, IL 60291 Email: mcolton@valdren.example Phone: 312-555-0148 Mobile: (414) 555-0193 Website: www.valdren.example

```html
<!DOCTYPE html>
<html lang="en">
<head>
<meta charset="utf-8">
<title>Valdren Business Card</title>
<link href="https://fonts.googleapis.com/css2?family=Open+Sans:wght@400;700&display=swap" rel="stylesheet">
<style>
  :root {
    --backdrop: #c9c9c9;
    --card-dark: #212121;
    --brand-orange: #f37021;
    --brand-orange-light: #f7963d;
    --text-light: #ffffff;
    --card-radius: 26px;
  }
  html, body {
    margin: 0;
    padding: 0;
    width: 1200px;
    height: 896px;
    overflow: hidden;
    background: var(--backdrop);
    font-family: "Open Sans", Arial, sans-serif;
  }
  .canvas {
    position: relative;
    width: 1200px;
    height: 896px;
  }
  .card {
    position: absolute;
    left: 334px;
    width: 528px;
    height: 301px;
    border-radius: var(--card-radius);
    overflow: hidden;
    box-shadow: 0 10px 22px rgba(0,0,0,0.22);
  }
  .card-front { top: 125px; background: var(--card-dark); }
  .card-back  { top: 475px; background: var(--brand-orange); }

  .wordmark {
    position: absolute;
    left: 24px;
    top: 6px;
    margin: 0;
    font-size: 58px;
    font-weight: 400;
    letter-spacing: 0.5px;
    color: var(--brand-orange);
    line-height: 1;
  }
  .accent-bar {
    position: absolute;
    left: 0;
    top: 99px;
    width: 16px;
    height: 38px;
    background: var(--brand-orange);
  }
  .person-name {
    position: absolute;
    left: 25px;
    top: 92px;
    margin: 0;
    font-size: 22px;
    font-weight: 700;
    color: var(--brand-orange);
    line-height: 1.2;
  }
  .company-name {
    position: absolute;
    left: 25px;
    top: 119px;
    margin: 0;
    font-size: 14px;
    color: var(--text-light);
  }
  .contact-list {
    position: absolute;
    left: 20px;
    top: 149px;
    margin: 0;
    padding: 0;
    list-style: none;
  }
  .contact-item {
    display: flex;
    align-items: center;
    height: 20px;
    font-size: 14.5px;
    color: var(--text-light);
  }
  .contact-icon {
    width: 12px;
    height: 12px;
    margin-right: 7px;
    fill: var(--brand-orange);
  }
  .address {
    position: absolute;
    left: 21px;
    top: 238px;
    margin: 0;
    font-style: normal;
    font-size: 14.5px;
    line-height: 20px;
    color: var(--text-light);
  }
  .brand-mark {
    position: absolute;
    left: 292px;
    top: 95px;
    width: 180px;
    height: 180px;
    border-radius: 50%;
    background: var(--brand-orange);
  }

  .back-pattern {
    position: absolute;
    inset: 0;
    background: linear-gradient(135deg, #f47a2c 0%, var(--brand-orange) 55%, #ea6a1e 100%);
  }
  .back-wordmark {
    position: absolute;
    left: 362px;
    top: 220px;
    margin: 0;
    font-size: 26px;
    font-weight: 400;
    color: var(--text-light);
    line-height: 1;
  }
</style>
</head>
<body>
<main class="canvas">
  <section class="card card-front" aria-label="Business card front">
    <p class="wordmark">Valdren</p>
    <div class="accent-bar"></div>
    <h1 class="person-name">Marisa Colton</h1>
    <p class="company-name">Valdren</p>
    <ul class="contact-list">
      <li class="contact-item">
        <svg class="contact-icon" viewBox="0 0 12 12" aria-hidden="true"><path d="M3 0h6a1 1 0 0 1 1 1v10a1 1 0 0 1-1 1H3a1 1 0 0 1-1-1V1a1 1 0 0 1 1-1zm.5 1.5v8h5v-8z"/></svg>
        (414) 555-0193
      </li>
      <li class="contact-item">
        <svg class="contact-icon" viewBox="0 0 12 12" aria-hidden="true"><path d="M2.4 0.5 4.3 2.6 3.3 4.1c.6 1.8 2 3.3 3.9 4.2l1.4-1 2.1 1.9-1.3 1.9C5.6 11 1 6.4.8 2z"/></svg>
        312-555-0148
      </li>
      <li class="contact-item">
        <svg class="contact-icon" viewBox="0 0 12 12" aria-hidden="true"><path d="M0 2.5h12v1L6 7 0 3.5zM0 4.8l6 3.5 6-3.5V10H0z"/></svg>
        mcolton@valdren.example
      </li>
      <li class="contact-item">
        <svg class="contact-icon" viewBox="0 0 12 12" aria-hidden="true"><circle cx="6" cy="6" r="5.5"/></svg>
        www.valdren.example
      </li>
    </ul>
    <address class="address">4318 N Fable Avenue<br>Oak Terrace, IL 60291</address>
    <div class="brand-mark" aria-hidden="true"></div>
  </section>

  <section class="card card-back" aria-label="Business card back">
    <div class="back-pattern" role="img" aria-label="Repeating embossed brand name pattern in tonal orange"></div>
    <p class="back-wordmark">Valdren</p>
  </section>
</main>
</body>
</html>
```